Brasko Construction Business Card

I need a business card design for my company.
We are a construction/machinery company.
I would like to see my logo on the front of the card and my details on the other side
I would like the card to be black or dark grey in colour,with my logo as i send it or modified with a lighter blue colour
I would like to see the design kept fairly simple,but eye catching at the same time
Industry/Entity Type
Business
Contact Information for Business Card
Name
Phone Number
Address
Email
Colors
00a990
1b1b1b
000000
474747
ececec

```html
<!DOCTYPE html>
<html lang="en">
<head>
<meta charset="utf-8">
<title>Brasko Construction Business Card</title>
<link rel="stylesheet" href="https://fonts.googleapis.com/css2?family=Ubuntu:wght@400;500;700&display=swap">
<style>
  :root {
    --page-bg: #474747;
    --card-black: #000000;
    --ink-white: #ffffff;
    --ink-soft: #ececec;
    --art-light: #ececec;
    --art-mid: #9a9a9a;
  }
  * { box-sizing: border-box; margin: 0; padding: 0; }
  html, body {
    width: 1105px;
    height: 1200px;
    overflow: hidden;
    background: var(--page-bg);
    font-family: "Ubuntu", sans-serif;
  }
  .card {
    position: absolute;
    left: 196px;
    width: 720px;
    height: 412px;
    background: var(--card-black);
    overflow: hidden;
  }
  .card--front { top: 145px; }
  .card--back { top: 601px; }

  .accent-bar {
    position: absolute;
    left: 0;
    top: 131px;
    width: 11px;
    height: 46px;
    background: var(--ink-white);
  }
  .contact {
    position: absolute;
    left: 50px;
    top: 128px;
    color: var(--ink-white);
  }
  .contact__name {
    font-size: 25px;
    font-weight: 500;
    line-height: 1.2;
  }
  .contact__role {
    font-size: 19px;
    color: var(--ink-soft);
    margin-top: 2px;
    margin-bottom: 16px;
  }
  .contact__line {
    font-size: 18px;
    line-height: 1.35;
  }
  .contact__row {
    display: flex;
    align-items: center;
    gap: 9px;
    font-size: 18px;
    margin-top: 12px;
  }
  .contact__row + .contact__row { margin-top: 8px; }
  .contact__row svg { width: 17px; height: 17px; fill: var(--ink-white); flex: none; }

  .brand-name {
    position: absolute;
    width: 262px;
    color: var(--ink-white);
    font-family: "Ubuntu", sans-serif;
    font-weight: 700;
    text-transform: uppercase;
    text-align: center;
    line-height: 1;
  }
  .brand-name__main { display: block; font-size: 46px; letter-spacing: 9px; margin-right: -9px; }
  .brand-name__sub { display: block; font-size: 20px; letter-spacing: 7px; margin-right: -7px; margin-top: 6px; }
  .card--front .brand-name { left: 400px; top: 232px; }
  .card--back .brand-name { left: 400px; top: 312px; }

  .machine-art {
    position: absolute;
    left: 0;
    top: 44px;
    width: 536px;
    height: 250px;
    background: linear-gradient(135deg, var(--art-light) 0%, var(--art-mid) 100%);
  }
</style>
</head>
<body>
  <section class="card card--front" aria-label="Business card front">
    <div class="accent-bar"></div>
    <div class="contact">
      <p class="contact__name">Daniel Reeve</p>
      <p class="contact__role">CEO/Founder</p>
      <p class="contact__line">4120 Harbor Ridge Road</p>
      <p class="contact__line">Juneau, Alaska 99801</p>
      <p class="contact__row">
        <svg viewBox="0 0 24 24" aria-hidden="true"><path d="M6.6 10.8a15.1 15.1 0 0 0 6.6 6.6l2.2-2.2a1 1 0 0 1 1-.25 11.4 11.4 0 0 0 3.6.57 1 1 0 0 1 1 1V20a1 1 0 0 1-1 1A17 17 0 0 1 3 4a1 1 0 0 1 1-1h3.5a1 1 0 0 1 1 1c0 1.25.2 2.45.57 3.6a1 1 0 0 1-.25 1z"/></svg>
        907 512 3846
      </p>
      <p class="contact__row">
        <svg viewBox="0 0 24 24" aria-hidden="true"><path d="M2 5h20v14H2z M2 5l10 8 10-8" fill="none" stroke="#fff" stroke-width="2"/><path d="M2 5h20L12 12z"/></svg>
        daniel@braskobuild.com
      </p>
    </div>
    <div class="brand-name">
      <span class="brand-name__main">Brasko</span>
      <span class="brand-name__sub">Construction</span>
    </div>
  </section>

  <section class="card card--back" aria-label="Business card back">
    <div class="machine-art" role="img" aria-label="Large white excavator arm and bucket illustration"></div>
    <div class="brand-name">
      <span class="brand-name__main">Brasko</span>
      <span class="brand-name__sub">Construction</span>
    </div>
  </section>
</body>
</html>
```